designing a website for a vacation beach house rental

We are buying a vacation rental on an awesome beach on the Isle of Palms in South Carolina. The closing is not until November 30 so we will only have the photos from the current home and we can change the photos once we move our furniture in. We want the website to be exciting and interactive and for people to be able to go to a chatterly page (that needs to be created) and the name of the beach house needs to be created (the address is 462 Marlowe Crescent, Isle of Palms. We need to be able to take this site and add it to KLNZ and StayNest and Dune Q&Q and other travel sites. We need the person that clicks on it to be hooked from the first second. We think this one is pretty good but we want ours way better http://gullrestcottage.example/ The price per week will be $7200 so the website needs to be elegant, stunning, all inclusive, retreat, relaxing, friends and family, eating together, amazing food town, beaches, golf, cocktails, wine, restaurants, history, architecture, opulence, Look up Charleston, SC to get an idea of what the area is all about. Top Chefs and top wines.

Target Market(s)

Upper class families with children; classy dressing; golfers; foodies; wine lovers; in shaper beach goers living the dream of a gorgeous beach house with friends and family at the pool, eating together, beach together, cooking together, playing games, walking on the beach, running on the beach, watching the sunset on the beach

Industry/Entity Type

House

Logo Text

the look and feel of an upper class family on vacation in an exclusive resort

Number of Pages Required

5+ page

Font styles to use
Serif

Requirements
Must have
• Lots of photos and movement; easy for me to update is a MUST; easy for a guest to register for staying; a calendar that will update automatically when someone pays; ability to take credit cards and CoinTap; guest book; keep up with the number of visits; all of the bells and whistles of the most modern websites; also works on any device like Zelphone or Zelpad or any smartphone

```html
<!DOCTYPE html>
<html lang="en">
<head>
<meta charset="utf-8">
<title>Marlowe Dunes Beach House</title>
<link href="https://fonts.googleapis.com/css2?family=Gelasio:ital,wght@0,400;0,500;1,400;1,500&display=swap" rel="stylesheet">
<style>
:root{
  --blue:#6f8ba6;
  --blue-dark:#5c7894;
  --text:#7690aa;
  --pale:#eef3f7;
  --panel:#f0f3f6;
  --band:#d7dfe5;
  --white:#ffffff;
  --photo-sky:#a9c3d8;
  --photo-room:#8d98a3;
  --photo-house:#6f8f6a;
  --photo-sea:#9fc1d6;
}
*{margin:0;padding:0;box-sizing:border-box}
html,body{width:1200px;height:3315px;overflow:hidden;background:var(--white)}
body{position:relative;font-family:"Gelasio",Georgia,serif;color:var(--text)}
.abs{position:absolute}
.photo{position:absolute}
.center{text-align:center}
.header{position:absolute;left:0;top:0;width:1200px;height:152px;background:var(--pale)}
.brand{position:absolute;left:100px;top:62px;width:130px;text-align:center;color:var(--blue)}
.brand-name{font-style:italic;font-size:20px;line-height:22px}
.brand-sub{font-size:11px;line-height:14px}
.nav{position:absolute;left:580px;top:92px;display:flex}
.nav a{display:block;padding:0 20px;font-style:italic;font-size:18px;line-height:36px;color:var(--blue-dark);text-decoration:none;border-left:1px solid #dfe6ec}
.nav a:first-child{border-left:none;color:var(--blue)}
.tile{position:absolute;display:flex;align-items:center;justify-content:center;font-style:italic;font-size:24px;line-height:30px;text-align:center}
.tile-light{background:#dbe7ee;color:var(--blue)}
.tile-dark{background:#8c9fb6;color:var(--white)}
.kicker{font-style:italic;font-size:26px;color:var(--blue)}
.title{font-size:48px;letter-spacing:1px;color:var(--blue);text-transform:uppercase}
.lead{font-size:13px;line-height:17px;color:var(--blue-dark)}
.feature{position:absolute;width:220px;text-align:center}
.feature svg{display:block;margin:0 auto}
.feature h3{margin-top:22px;font-style:italic;font-weight:500;font-size:17px;line-height:29px;letter-spacing:1px;color:var(--blue-dark);text-transform:uppercase}
.feature p{margin-top:20px;font-size:12.5px;line-height:17px;color:#98aec2}
.btn{position:absolute;background:var(--blue);color:var(--white);font-size:17px;letter-spacing:1px;text-transform:uppercase;display:flex;align-items:center;justify-content:center}
.panel{position:absolute;left:93px;width:1014px;background:var(--panel)}
.small-heading{font-size:22px;letter-spacing:4px;text-transform:uppercase;color:var(--blue-dark)}
.footer-h{position:absolute;font-size:21px;letter-spacing:2px;text-transform:uppercase;color:var(--blue-dark)}
.links{position:absolute;list-style:none;font-size:13px;line-height:24px;color:var(--blue-dark)}
.links li::before{content:"";display:inline-block;width:6px;height:6px;background:var(--blue);margin-right:14px;vertical-align:middle}
.gallery{position:absolute;left:610px;top:3052px;width:270px;height:159px;display:grid;grid-template-columns:repeat(3,1fr);grid-template-rows:repeat(3,1fr);gap:2px}
.gallery div{background:linear-gradient(135deg,#c9a27a,#8aa6b8)}
.gallery div:nth-child(2n){background:linear-gradient(135deg,#e0b060,#b07a4a)}
.gallery div:nth-child(3n){background:linear-gradient(135deg,#7fa7c0,#d9c0a0)}
.copyright{position:absolute;left:0;top:3255px;width:1200px;height:60px;background:var(--band);font-size:12px;letter-spacing:1px;color:var(--blue-dark);display:flex;align-items:center;justify-content:center}
</style>
</head>
<body>

<header class="header">
  <div class="brand">
    <div class="brand-name">Marlowe Dunes</div>
    <div class="brand-sub">Beach House</div>
  </div>
  <nav class="nav">
    <a>Home</a><a>Rooms</a><a>Services</a><a>Packages</a><a>Contacts</a>
  </nav>
</header>

<section class="hero">
  <div class="photo" role="img" aria-label="Bright living room with blue sofas and ceiling fan" style="left:104px;top:166px;width:495px;height:327px;background:linear-gradient(160deg,#dfe6ea,var(--photo-room) 70%,#5f6f86)"></div>
  <div class="tile tile-light" style="left:608px;top:166px;width:234px;height:170px">Cool and relaxing<br>view from terrace</div>
  <div class="photo" role="img" aria-label="Terrace with chairs under blue sky" style="left:851px;top:166px;width:247px;height:170px;background:linear-gradient(160deg,#3f7fc4,#a9c8d6 60%,#6e8a7a)"></div>
  <div class="photo" role="img" aria-label="Three-storey beach house among palm trees" style="left:608px;top:345px;width:490px;height:318px;background:linear-gradient(180deg,#5f9ad6,#c8d4d8 45%,var(--photo-house))"></div>
  <div class="tile tile-dark" style="left:102px;top:504px;width:249px;height:159px">Clean, elegant<br>and refreshing</div>
  <div class="photo" role="img" aria-label="Open kitchen and dining area" style="left:360px;top:504px;width:239px;height:159px;background:linear-gradient(160deg,#c7ccd0,#8a6f5a 60%,#6f7d96)"></div>
</section>

<section class="welcome">
  <div class="abs center kicker" style="left:0;top:738px;width:1200px">Welcome to</div>
  <h1 class="abs center title" style="left:0;top:770px;width:1200px;font-weight:400">Marlowe Dunes Beach House</h1>
  <p class="abs center lead" style="left:230px;top:842px;width:740px">voluptatum deleniti atque corrupti quos dolores et quas molestias excepturi sint occaecati cupiditate non provident, similique sunt in culpa qui officia deserunt mollitia animi, id est laborum et dolorum fuga. Et harum quidem rerum facilis est et expedita distinctio.</p>
</section>

<section class="features">
  <div class="feature" style="left:87px;top:992px">
    <svg width="60" height="50" viewBox="0 0 60 50"><rect x="20" y="4" width="20" height="8" fill="none" stroke="#6f8ba6" stroke-width="3"/><rect x="2" y="12" width="56" height="36" fill="#6f8ba6"/></svg>
    <h3>Special<br>Promotion</h3>
    <p>Nam libero tempore, cum soluta nobis est eligendi optio cumque nihil impedit quo minus id quod maxime placeat facere possimus, omnis voluptas assumendadest, omnis dolor repellendus.</p>
  </div>
  <div class="feature" style="left:361px;top:977px">
    <svg width="70" height="65" viewBox="0 0 70 65"><path d="M28 4c-4 5 4 7 0 12M36 4c-4 5 4 7 0 12" fill="none" stroke="#6f8ba6" stroke-width="2"/><path d="M10 24h44v12a22 18 0 0 1-44 0z" fill="#6f8ba6"/><path d="M54 28h6a6 6 0 0 1 0 12h-8" fill="none" stroke="#6f8ba6" stroke-width="3"/><rect x="4" y="56" width="58" height="4" rx="2" fill="#6f8ba6"/></svg>
    <h3>Bed &amp; Breakfast<br>Package</h3>
    <p>Nam libero tempore, cum soluta nobis est eligendi optio cumque nihil impedit quo minus id quod maxime placeat facere possimus, omnis voluptas assumendadest, omnis dolor repellendus.</p>
  </div>
  <div class="feature" style="left:646px;top:992px">
    <svg width="58" height="58" viewBox="0 0 58 58"><circle cx="29" cy="29" r="27" fill="#6f8ba6"/><circle cx="29" cy="29" r="20" fill="none" stroke="#fff" stroke-width="2"/><path d="M23 16v26M20 16v8a3 3 0 0 0 6 0v-8M35 16c4 2 4 10 0 12v14" fill="none" stroke="#fff" stroke-width="2"/></svg>
    <h3>Hotel<br>Restaurant</h3>
    <p>Nam libero tempore, cum soluta nobis est eligendi optio cumque nihil impedit quo minus id quod maxime placeat facere possimus, omnis voluptas assumendadest, omnis dolor repellendus.</p>
  </div>
  <div class="feature" style="left:900px;top:998px">
    <svg width="72" height="46" viewBox="0 0 72 46"><path d="M4 6c12-4 22-2 32 6v30c-10-8-20-10-32-6z M68 6c-12-4-22-2-32 6v30c10-8 20-10 32-6z" fill="#6f8ba6"/><path d="M2 40c12-3 22-1 34 5 12-6 22-8 34-5" fill="none" stroke="#6f8ba6" stroke-width="2"/></svg>
    <h3>Sign up for<br>our Guestbook</h3>
    <p>Nam libero tempore, cum soluta nobis est eligendi optio cumque nihil impedit quo minus id quod maxime placeat facere possimus, omnis voluptas assumendadest, omnis dolor repellendus.</p>
  </div>
  <div class="btn" style="left:486px;top:1333px;width:230px;height:48px">See where we are</div>
</section>

<section class="panel" style="top:1432px;height:583px">
  <div class="photo" role="img" aria-label="Couple sitting together on a sunny beach by the sea" style="left:17px;top:53px;width:482px;height:488px;background:linear-gradient(180deg,#7fb0dc,var(--photo-sea) 45%,#5f96b8 55%,#eadfcc 62%,#f3ece0)"></div>
  <div class="abs center kicker" style="left:560px;top:88px;width:370px;font-size:30px">Itaque earum</div>
  <div class="abs center title" style="left:560px;top:118px;width:370px;font-size:56px">Rerumhic</div>
  <svg class="abs" style="left:727px;top:210px" width="40" height="36" viewBox="0 0 40 36"><path d="M4 14a16 12 0 0 1 32 0z" fill="#6f8ba6"/><path d="M20 14l-6 16" stroke="#6f8ba6" stroke-width="2"/><path d="M0 32c8-4 28-4 40 0v4H0z" fill="#6f8ba6"/></svg>
  <p class="abs center lead" style="left:580px;top:282px;width:330px">Sed ut perspiciatis unde omnis iste natus error sit voluptatem accusantium doloremque laudantium.</p>
  <p class="abs center lead" style="left:570px;top:336px;width:350px">Nemo enim ipsam voluptatem quia voluptas sit aspernatur aut odit aut fugit, sed quia consequuntur magni dolores eos qui ratione voluptatem sequi nesciunt. Neque porro quisquam est, qui dolorem ipsum quia dolor sit amet, consectetur, adipisci velit, sed quia non numquam eius modi tempora incidunt ut labore et dolore magnam aliquam quaerat voluptatem.</p>
  <div class="btn" style="left:623px;top:475px;width:243px;height:51px">See where we are</div>
</section>

<section class="testimonial">
  <div class="abs center small-heading" style="left:0;top:2088px;width:1200px">Our customers love us</div>
  <svg class="abs" style="left:573px;top:2142px" width="54" height="38" viewBox="0 0 54 38"><path d="M2 2h20v18c0 10-6 16-16 18l-2-5c6-2 8-6 8-11H2z M32 2h20v18c0 10-6 16-16 18l-2-5c6-2 8-6 8-11H32z" fill="#6f8ba6"/></svg>
  <p class="abs center lead" style="left:190px;top:2252px;width:820px;color:#a2b5c7">Et harum quidem rerum facilis est et expedita distinctio. Nam libero tempore, cum soluta nobis est eligendi optio cumque nihil impedit quo minus id quod maxime placeat facere possimus, omnis voluptas assumenda est, omnis dolor repellendus. Temporibus autem quibusdam et aut officiis debitis aut rerum necessitatibus saepe eveniet ut et voluptates repudiandae sint et molestiae non recusandae. Itaque earum rerum hic tenetur a sapiente delectus, ut aut reiciendis voluptatibus maiores alias consequatur aut perferendis doloribus asperiores repellat</p>
  <div class="abs center" style="left:0;top:2370px;width:1200px;font-style:italic;font-size:24px;color:#a2b5c7">Della Whitford</div>
</section>

<section class="panel" style="top:2449px;height:473px;background:#f3f4f5">
  <div class="photo" role="img" aria-label="Faint background of a set dining table" style="left:0;top:0;width:1014px;height:473px;background:radial-gradient(ellipse at 60% 40%,#eceeef,#f5f6f7 70%)"></div>
  <svg class="abs" style="left:472px;top:140px" width="74" height="56" viewBox="0 0 74 56"><circle cx="28" cy="6" r="4" fill="#6f8ba6"/><path d="M4 34a24 24 0 0 1 48 0z" fill="#6f8ba6"/><rect x="0" y="36" width="56" height="4" fill="#6f8ba6"/><path d="M50 38l10 12h14" fill="none" stroke="#6f8ba6" stroke-width="5"/></svg>
  <div class="abs center" style="left:0;top:228px;width:1014px;font-style:italic;font-size:35px;line-height:40px;letter-spacing:1px;color:var(--blue-dark)">AT VERO EOS ET ACCUSAMUS ET IUSTO<br>ODIO DIGNISSIMOS DUCIMUS</div>
  <div class="btn" style="left:429px;top:336px;width:154px;height:50px">See more</div>
</section>

<footer>
  <div class="panel" style="top:2955px;height:300px"></div>
  <div class="footer-h" style="left:126px;top:3008px">Useful links</div>
  <ul class="links" style="left:126px;top:3052px">
    <li>Temporibus autem</li><li>Quibusdam et aut</li><li>Officiis debitis</li><li>Aut rerum</li><li>Necessitatibus saepe</li><li>Eveniet ut et voluptates</li><li>Repudiandae sint et</li>
  </ul>
  <ul class="links" style="left:358px;top:3040px">
    <li>Molestiae non recusandae</li><li>Itaque earum rerum hic tenetur</li><li>A sapiente delectus, ut aut</li><li>Reiciendis voluptatibus</li><li>Maiores alias consequatur</li><li>Aut perferendis</li><li>Doloribus asperiores</li>
  </ul>
  <div class="footer-h" style="left:610px;top:3008px">Gallery</div>
  <div class="gallery" role="img" aria-label="Gallery of beach, food and house photos">
    <div></div><div></div><div></div><div></div><div></div><div></div><div></div><div></div><div></div>
  </div>
  <div class="footer-h" style="left:924px;top:3008px">Mission</div>
  <p class="abs lead" style="left:924px;top:3052px;width:180px;line-height:19px">Nemo enim ipsam voluptatem quia voluptas sit aspernatur aut odit aut fugit, sed quia consequuntur magni dolores eos qui ratione voluptatem sequi nesciunt.</p>
  <div class="copyright">© 2015 Marlowe Dunes Beach House</div>
</footer>

</body>
</html>
```